Business card for wedding & event planning company

I'm looking for a well designed double sided business card to represent my wedding and event planning company.

It should include the fact we manage the following events:
Weddings, birthdays, conferences, product launches, fashion shows & conventions
in the following areas:
Wiltshire, Oxfordshire, Berkshire & London

My contact details to be included are:

Moira Pennock
07715 482036
moira@amberlarkcelebrations.co.uk
www.amberlarkcelebrations.co.uk

My logo can be found at the following Filevaultex location:
AI file: https://www.filevaultex.com/s/k4mprt8wn31b7hz/brandlogo_sourcefile.ai?dl=0
PNG file:
https://www.filevaultex.com/s/h9qsle2vbx07mnd/brandlogo_image.png?dl=0

Target Market(s)

women aged 30-55

Industry/Entity Type

Wedding

Contact Information for Business Card

in the following areas:

Moira Pennock
Event Planner
07715 482036

Font styles to use
Serif
Sans Serif
Script

Requirements
Must have
• Purple and white colour scheme
Should not have
• Black background
• Please don't submit any of the see-through business card designs.

```html
<!DOCTYPE html>
<html lang="en">
<head>
<meta charset="utf-8">
<title>Amber Lark Celebrations — Business Card</title>
<link href="https://fonts.googleapis.com/css2?family=Pinyon+Script&display=swap" rel="stylesheet">
<style>
  :root {
    --purple: #8a2f91;
    --white: #ffffff;
    --ink-light: #f6eef7;
    --canvas: #e9e9eb;
    --rule: #c9a9cc;
  }
  * { box-sizing: border-box; margin: 0; padding: 0; }
  html, body {
    width: 1200px; height: 1000px; overflow: hidden;
    background: var(--canvas);
  }
  .sheet {
    position: relative; width: 1200px; height: 1000px;
    display: flex; flex-direction: column; align-items: center;
    justify-content: center; gap: 60px;
  }
  .card {
    position: relative; width: 700px; height: 400px;
    background: var(--white); overflow: hidden;
    box-shadow: 0 6px 18px rgba(0,0,0,0.12);
  }
  .brand {
    display: flex; align-items: center; gap: 14px;
    font-family: "Pinyon Script", cursive;
    color: var(--purple); font-size: 38px; line-height: 1.05;
  }
  .brand-name { display: block; }
  .brand-dot {
    width: 26px; height: 26px; border-radius: 50%;
    background: var(--purple); flex: none;
  }
  .brand-rule { height: 1px; background: var(--rule); margin-top: 12px; }

  /* front */
  .front-brand {
    position: absolute; left: 0; top: 0; width: 340px; height: 400px;
    display: flex; flex-direction: column; justify-content: center;
    padding: 0 40px 70px 40px;
  }
  .contact-panel {
    position: absolute; left: 340px; top: 0; width: 360px; height: 400px;
    background: var(--purple); color: var(--ink-light);
    font-family: "Pinyon Script", cursive;
    padding: 90px 24px 0 40px;
  }
  .contact-name { font-size: 44px; line-height: 1; margin-bottom: 34px; }
  .contact-line { font-size: 21px; line-height: 1.5; white-space: nowrap; }

  /* back */
  .back-head {
    position: absolute; left: 0; top: 0; width: 700px; height: 180px;
    display: flex; align-items: center; justify-content: flex-end;
    padding-right: 120px;
  }
  .back-head .brand-wrap { width: 280px; }
  .services-band {
    position: absolute; left: 0; top: 180px; width: 700px; height: 220px;
    background: var(--purple); color: var(--ink-light);
    font-family: "Pinyon Script", cursive;
    font-size: 21px; line-height: 1.5; padding: 24px 40px 0 40px;
  }
</style>
</head>
<body>
<main class="sheet">
  <section class="card card-front" aria-label="Business card front">
    <div class="front-brand">
      <div class="brand"><span class="brand-dot"></span><span class="brand-name">Amber Lark<br>Celebrations</span></div>
      <div class="brand-rule"></div>
    </div>
    <div class="contact-panel">
      <p class="contact-name">Moira Pennock</p>
      <p class="contact-line">07715 482036</p>
      <p class="contact-line">moira@amberlarkcelebrations.co.uk</p>
      <p class="contact-line">www.amberlarkcelebrations.co.uk</p>
    </div>
  </section>

  <section class="card card-back" aria-label="Business card back">
    <div class="back-head">
      <div class="brand-wrap">
        <div class="brand"><span class="brand-dot"></span><span class="brand-name">Amber Lark<br>Celebrations</span></div>
        <div class="brand-rule"></div>
      </div>
    </div>
    <div class="services-band">
      <p>Weddings, birthdays, conferences, product launches, fashion shows &amp; conventions in the following areas:</p>
      <p>Wiltshire, Oxfordshire, Berkshire &amp; London</p>
    </div>
  </section>
</main>
</body>
</html>
```